refurbishment of diamond cut alloy wheels

we need to design a flyer that will catch the eye of the customer to refurbish diamond cut alloy wheels. we refurbish the wheels by using the latest CNC machine to precision cut and resurface the wheel. we would like before and after pictures of maybe Valtorin, KRZ, Ovel wheels to give it a prestige look. The final design should communicate an expensive look and providing a good image for the business. The colours that I would like to use is black and red which should make the flyer stand out. The logo must sit on a black background without the wordings of specialists in TQ, Ovel etc and also without servicing, diagnostics etc as well. This flyer is just to communicate refurbishment of alloy wheels to high standard.

Target Market(s)

any members of the public and car dealerships

Industry/Entity Type

Automotive

Colors

Designer to choose colors to be used in the design.

Requirements
Must have
• Wow factor with great images of wheels
Nice to have
• Maybe on the front of the flyer it has a picture of a wheel and then on the back of the flyer it has before and after pictures to show how just how incredible it is to refurbish wheels
Should not have
• other makes of wheels apart from KRZ, Ovel, and any other high end makes of vehicles wheels

```html
<!DOCTYPE html>
<html lang="en">
<head>
<meta charset="utf-8">
<title>Crestline Motors – Alloy Wheel Refurbishment Flyer</title>
<link href="https://fonts.googleapis.com/css2?family=Archivo+Black&family=Open+Sans:wght@400;600;700&display=swap" rel="stylesheet">
<style>
  :root {
    --backdrop: #9a9a9a;
    --black: #0b0b0b;
    --panel-dark: #151515;
    --red: #c1272d;
    --red-deep: #8e1519;
    --silver: #d9d9d9;
    --silver-dark: #8c8c8c;
    --white: #ffffff;
    --muted: #cfcfcf;
  }
  * { margin: 0; padding: 0; box-sizing: border-box; }
  html, body { width: 1200px; height: 3261px; overflow: hidden; }
  body { background: var(--backdrop); font-family: "Open Sans", Arial, sans-serif; position: relative; }

  .flyer-page {
    position: absolute; left: 42px; width: 1116px; height: 1562px;
    background: var(--black); overflow: hidden;
    box-shadow: 0 6px 18px rgba(0,0,0,.45);
  }
  .flyer-page--front { top: 42px; }
  .flyer-page--back { top: 1657px; }
  .page-art { position: absolute; inset: 0; width: 1116px; height: 1562px; }

  .brand {
    position: absolute; display: flex; align-items: center; gap: 18px;
    background: var(--panel-dark); padding: 0 28px;
  }
  .brand-mark { width: 40px; height: 40px; background: var(--red); flex: none; }
  .brand-name {
    font-family: "Archivo Black", Arial, sans-serif; color: var(--white);
    font-size: 38px; line-height: 1.05; letter-spacing: 1px;
  }
  .flyer-page--front .brand { left: 49px; top: 88px; width: 398px; height: 131px; }
  .flyer-page--back .brand { left: 49px; top: 55px; width: 300px; height: 100px; }
  .flyer-page--back .brand-name { font-size: 29px; }
  .flyer-page--back .brand-mark { width: 30px; height: 30px; }

  .front-title {
    position: absolute; left: 495px; top: 72px; width: 600px;
    font-family: "Archivo Black", Arial, sans-serif; font-size: 60px; line-height: 76px;
    text-transform: uppercase; color: var(--silver); letter-spacing: 1px;
  }
  .front-claim {
    position: absolute; left: 60px; right: 60px; top: 1090px;
    color: var(--white); font-weight: 700; font-size: 33px; line-height: 46px; text-align: center;
  }
  .front-contact-note {
    position: absolute; left: 120px; top: 1405px; width: 420px;
    color: var(--muted); font-size: 25px; line-height: 34px;
  }
  .phone-button {
    position: absolute; display: flex; align-items: center; justify-content: center; gap: 16px;
    background: linear-gradient(#d23238, var(--red-deep)); border: 3px solid #e06a6e;
    border-radius: 16px; color: var(--white); font-weight: 700;
  }
  .phone-button svg { fill: var(--white); }
  .flyer-page--front .phone-button { left: 587px; top: 1383px; width: 437px; height: 94px; font-size: 42px; }
  .flyer-page--back .phone-button { left: 603px; top: 1423px; width: 398px; height: 91px; font-size: 39px; }

  .back-title {
    position: absolute; left: 473px; top: 88px; width: 600px;
    color: var(--white); font-weight: 600; font-size: 44px; line-height: 56px;
  }
  .result-label {
    position: absolute; top: 838px; height: 59px; width: 265px;
    background: var(--red); border-radius: 8px; border: 2px solid #e06a6e;
    color: var(--white); font-weight: 600; font-size: 30px; line-height: 55px; text-align: center;
  }
  .result-label--before { left: 49px; }
  .result-label--after { left: 512px; }
  .coverage {
    position: absolute; left: 40px; right: 40px; top: 932px;
    color: var(--white); font-weight: 700; font-size: 26px; line-height: 40px; text-align: center;
  }
  .back-rule { position: absolute; left: 210px; right: 210px; top: 1076px; height: 2px; background: var(--silver); }
  .back-copy {
    position: absolute; left: 80px; right: 80px; top: 1098px;
    color: var(--muted); font-size: 18px; line-height: 25px; text-align: center;
  }
  .back-copy p + p { margin-top: 14px; }
  .cta {
    position: absolute; left: 60px; top: 1435px; color: var(--white); line-height: 1.1;
  }
  .cta-lead { font-size: 22px; text-transform: uppercase; }
  .cta-main { font-size: 42px; text-transform: uppercase; }
</style>
</head>
<body>

<section class="flyer-page flyer-page--front">
  <svg class="page-art" viewBox="0 0 1116 1562" aria-hidden="false">
    <defs>
      <linearGradient id="frontRed" x1="0" y1="0" x2="0" y2="1">
        <stop offset="0" stop-color="#d0292f"/><stop offset="1" stop-color="#7f1216"/>
      </linearGradient>
      <linearGradient id="wheelTones" x1="0" y1="0" x2="1" y2="1">
        <stop offset="0" stop-color="#3b3b3b"/><stop offset=".5" stop-color="#151515"/><stop offset="1" stop-color="#4a4a4a"/>
      </linearGradient>
      <linearGradient id="wheelTonesYellow" x1="0" y1="0" x2="1" y2="1">
        <stop offset="0" stop-color="#c9a520"/><stop offset=".35" stop-color="#2a2a2a"/><stop offset="1" stop-color="#111"/>
      </linearGradient>
      <linearGradient id="silverLine" x1="0" y1="0" x2="1" y2="0">
        <stop offset="0" stop-color="#6e6e6e"/><stop offset=".5" stop-color="#f2f2f2"/><stop offset="1" stop-color="#6e6e6e"/>
      </linearGradient>
    </defs>
    <polygon points="0,0 490,0 440,50 0,50" fill="var(--red)"/>
    <rect x="0" y="330" width="1116" height="990" fill="url(#frontRed)"/>
    <polygon points="0,1320 1116,1320 1116,1060 820,1320" fill="#1a1a1a" opacity=".0"/>
    <polygon points="0,350 700,350 410,1060 0,900" fill="url(#wheelTonesYellow)" role="img" aria-label="Photo of a black alloy wheel on a yellow performance car"/>
    <polygon points="0,350 700,350 410,1060 0,900" fill="none" stroke="url(#silverLine)" stroke-width="8"/>
    <polygon points="740,350 1116,350 1116,1060 450,1060" fill="url(#wheelTones)" role="img" aria-label="Close-up photo of a black multi-spoke alloy wheel"/>
    <polygon points="740,350 1116,350 1116,1060 450,1060" fill="none" stroke="url(#silverLine)" stroke-width="8"/>
    <rect x="0" y="1316" width="1116" height="6" fill="url(#silverLine)"/>
  </svg>

  <div class="brand"><span class="brand-mark"></span><span class="brand-name">CRESTLINE<br>MOTORS</span></div>
  <h1 class="front-title">Alloy Wheel Refurbishment Specialists</h1>
  <p class="front-claim">We refurbish the wheels by using the latest CNC machine to precision cut and resurface the wheel.</p>
  <p class="front-contact-note">If you need premier Alloy Wheel Refurbishment services in Slough, please contact us:</p>
  <div class="phone-button">
    <svg width="36" height="36" viewBox="0 0 24 24"><path d="M6.6 10.8a15.1 15.1 0 0 0 6.6 6.6l2.2-2.2a1 1 0 0 1 1-.25 11.4 11.4 0 0 0 3.6.57 1 1 0 0 1 1 1V20a1 1 0 0 1-1 1A17 17 0 0 1 3 4a1 1 0 0 1 1-1h3.5a1 1 0 0 1 1 1c0 1.25.2 2.45.57 3.6a1 1 0 0 1-.25 1z"/></svg>
    <span>01632 960 418</span>
  </div>
</section>

<section class="flyer-page flyer-page--back">
  <svg class="page-art" viewBox="0 0 1116 1562">
    <defs>
      <linearGradient id="beforeTones" x1="0" y1="0" x2="1" y2="1">
        <stop offset="0" stop-color="#6b6258"/><stop offset=".5" stop-color="#3a3836"/><stop offset="1" stop-color="#8d8880"/>
      </linearGradient>
      <linearGradient id="afterTones" x1="0" y1="0" x2="1" y2="1">
        <stop offset="0" stop-color="#b9bcbf"/><stop offset=".5" stop-color="#3c3e42"/><stop offset="1" stop-color="#d6d8da"/>
      </linearGradient>
      <linearGradient id="silverLine2" x1="0" y1="0" x2="1" y2="0">
        <stop offset="0" stop-color="#6e6e6e"/><stop offset=".5" stop-color="#f2f2f2"/><stop offset="1" stop-color="#6e6e6e"/>
      </linearGradient>
      <linearGradient id="ctaRed" x1="0" y1="0" x2="1" y2="0">
        <stop offset="0" stop-color="#c1272d"/><stop offset="1" stop-color="#7f1216"/>
      </linearGradient>
    </defs>
    <polygon points="0,0 360,0 320,35 0,35" fill="var(--red)"/>
    <polygon points="0,160 0,650 200,260 200,160" fill="var(--red)"/>
    <polygon points="900,260 1116,260 1116,700" fill="var(--red)"/>
    <polygon points="120,285 560,285 450,822 0,822 0,540" fill="url(#beforeTones)" role="img" aria-label="Before photo: worn and corroded diamond cut alloy wheel"/>
    <polygon points="120,285 560,285 450,822 0,822 0,540" fill="none" stroke="url(#silverLine2)" stroke-width="7"/>
    <polygon points="620,285 1116,285 1116,822 510,822" fill="url(#afterTones)" role="img" aria-label="After photo: the same alloy wheel refurbished with a bright diamond cut finish"/>
    <polygon points="620,285 1116,285 1116,822 510,822" fill="none" stroke="url(#silverLine2)" stroke-width="7"/>
    <polygon points="0,1410 590,1410 540,1535 0,1535" fill="url(#ctaRed)"/>
  </svg>

  <div class="brand"><span class="brand-mark"></span><span class="brand-name">CRESTLINE<br>MOTORS</span></div>
  <h2 class="back-title">Alloy wheel Refurbishment Specialists in and around Slough</h2>
  <div class="result-label result-label--before">Before</div>
  <div class="result-label result-label--after">After</div>
  <p class="coverage">We cater to all locations in and around Colnbrook, Windsor, Hayes, Hounslow, Staines, Ascot and Ashford. For all car body modifications and restorations get in touch with our team of experts today!</p>
  <div class="back-rule"></div>
  <div class="back-copy">
    <p>If you are looking to refresh the look of your car but don't want the expense of new alloys, with a wide range of limited edition colours to choose from why not consider customising and refurbishing your existing alloys?</p>
    <p>If you've had your alloy wheels long enough for them to require alloy refurbishment you can choose from a wide range of colours for refurbishment or choose a brand new set from our comprehensive range. At Apex Wheels &amp; Tyres, we stock an extensive range of the latest designs from all the leading suppliers and manufacturers so you are sure to find a stylish new design.</p>
  </div>
  <div class="cta">
    <div class="cta-lead">If your alloys need refurbishment</div>
    <div class="cta-main">Contact us today</div>
  </div>
  <div class="phone-button">
    <svg width="34" height="34" viewBox="0 0 24 24"><path d="M6.6 10.8a15.1 15.1 0 0 0 6.6 6.6l2.2-2.2a1 1 0 0 1 1-.25 11.4 11.4 0 0 0 3.6.57 1 1 0 0 1 1 1V20a1 1 0 0 1-1 1A17 17 0 0 1 3 4a1 1 0 0 1 1-1h3.5a1 1 0 0 1 1 1c0 1.25.2 2.45.57 3.6a1 1 0 0 1-.25 1z"/></svg>
    <span>01632 960 418</span>
  </div>
</section>

</body>
</html>
```